Webdesign für ambulanten Intensivpflegedienst
Zielgruppe
Moin liebe Designer,
vorab einen guten Start ins neue Jahr :) Wir sind ein ambulanter Intensivpflegedienst im Speckgürtel Hamburgs. Wir betreuen seit über 20 Jahren Kinder, Jugendliche und Erwachsene, die eine dauerhafte Überwachung und Betreuung benötigen. Dabei sind unsere Pflegefachkräfte dauerhaft vor Ort. Wir haben kaum Fluktuation, eine hohe Mitarbeiterzufriedenheit und erhalten auch weiterhin Bewerbungen in diesem hart umkämpften Markt, leider ist es uns noch nicht gelungen diese positiven Aspekte öffentlichkeitswirksam nach außen zu tragen.
Aufgabenstellung
Neues Corporate Identity Design für eine Wordpress oder Joomla Seite.
Bilder können gerne aus bildmarktplatz-ost.com oder ähnlichen Marktplätzen vorgeschlagen werden. Dabei bitten wir auf Bilder mit älteren Menschen im Rollstuhl oder Pflegekräfte in Dienstkleidung zu verzichten, da unsere Mitarbeitenden unseren Kund:innen nicht das Bild einer Intensivstation vermitteln wollen, sondern ein würdiges Leben daheim oder unterwegs. Ebenso nutzen unsere Kund:innen Elektro-Rollstühle, sind mobil, gehen zur Schule oder in die Uni.
Gerne kann auch die Geschichte oder Bilder eines Betroffenen benutzt werden. Einige unserer Kund:innen spielen E-Rolli-Fußball: https://www.sportverband-muster.de/nachhaltigkeitsmanagement/news/news-detail/?tx_news_pi1%5Bnews%5D=648213 oder engagieren sich für benachteiligte.
Ein Gesichtsbuchs oder Bildfluss Account besteht nicht. Ein Nerv und KarriereNetz Profil sind im Aufbau.
Wir haben uns ein paar Websites angesehen, die auch unseren Wünschen entsprechen, diese können wir gerne auf Anfrage verschicken. Als Referenz unsere alte Website: https://seitenspeicher-beispiel.org/web/20190107114418/https://taleb-pflegedienst.de/ oder unsere aktuellen Stellenanzeigen: https://www.inseratbrett-muster.de/s-bestandsliste.html?userId=71564820
Als Thema/Farbkonzept für unsere Website würden wir gerne die Nähe zur Lüneburger Heide nutzen und auch in diesem Stil/ Farben etc. die Website gestalten. Beispielhaft kann dafür die Tourismusseite der Lüneburger Heide genommen werden: https://www.gruenland-ferien-beispiel.de/natur
Ersichtlich sind unsere Stellenanzeigen in blau gehalten und eher dem Wasser zugeneigt, wie auch unser Logo aus einem Fisch besteht und unsere alte Website eher an den ländlichen Raum. Da wir Kunden sowohl in Hamburg als auch in Schleswig-Holstein und zuletzt überwiegend in Niedersachsen (Lüneburger Heide) betreuen, würden wir uns freuen, wenn die Nähe zum Wasser und der Heide vereint werden kann.
Wir haben hier be..

```html
<!DOCTYPE html>
<html lang="de">
<head>
<meta charset="utf-8">
<title>Taleb Pflegedienst – Ambulante Intensivpflege</title>
<link href="https://fonts.googleapis.com/css2?family=Jost:ital,wght@0,400;0,500;0,600;1,300;1,400&family=Montserrat:wght@400;500;600&display=swap" rel="stylesheet">
<style>
:root{
  --blue:#2f5fc4;
  --blue-dark:#2a55b3;
  --blue-light:#4d7ad8;
  --pink:#c56ab9;
  --mist:#eef3f8;
  --ink:#1f2330;
  --grey:#6b7080;
  --white:#ffffff;
}
*{margin:0;padding:0;box-sizing:border-box}
html,body{width:1200px;height:4298px;overflow:hidden;background:var(--white)}
body{font-family:"Montserrat",sans-serif;color:var(--ink)}
.page{position:relative;width:1200px;height:4298px;overflow:hidden}
.abs{position:absolute}
.head{font-family:"Jost",sans-serif;font-weight:500}
.accent{color:var(--blue)}
.btn{position:absolute;display:flex;align-items:center;justify-content:center;border-radius:22px;font-family:"Jost",sans-serif;font-size:14px;color:var(--white)}
.btn-outline{border:2px solid var(--white)}
.btn-pink{background:var(--pink);box-shadow:0 6px 12px rgba(0,0,0,.15)}
.btn-blue{background:var(--blue)}
.eyebrow{position:absolute;font-size:11.5px;font-weight:600;letter-spacing:1px;color:var(--blue)}
.eyebrow svg{display:block;margin-top:4px}
.small{font-size:11.5px;line-height:18px;color:var(--grey)}

/* header & hero */
.hero{left:0;top:0;width:1200px;height:600px;background:linear-gradient(100deg,#2f5fc4 0%,#3a68cc 45%,#5b83d6 75%,#6f92dc 100%)}
.brand{display:flex;align-items:center;gap:10px;font-family:"Jost",sans-serif;font-size:20px;font-weight:500;color:var(--white)}
.brand .dot{width:14px;height:14px;border-radius:50%;background:var(--white)}
.nav{left:576px;top:24px;display:flex;gap:26px;font-family:"Jost",sans-serif;font-size:14px;color:var(--white);align-items:center}
.nav .contact{border:2px solid var(--white);border-radius:22px;padding:8px 30px;margin-left:8px}
.nav-line{left:150px;top:78px;width:900px;height:2px;background:rgba(255,255,255,.8)}
.hero-title{left:150px;top:196px;font-size:36px;line-height:45px;color:var(--white);font-weight:500;white-space:nowrap}
.hero-text{left:150px;top:302px;width:300px;font-size:11px;line-height:15px;font-weight:600;color:var(--white)}
.slider-dots{left:1038px;top:263px;display:flex;flex-direction:column;gap:9px}
.slider-dots span{width:9px;height:9px;border-radius:50%;background:rgba(255,255,255,.5)}
.slider-dots span:first-child{background:var(--blue)}

/* intro */
.photo-circle{border-radius:50%;border:2px solid var(--blue)}
.badge{left:905px;top:512px;width:110px;height:110px;border-radius:50%;background:var(--pink);color:var(--white);font-family:"Jost",sans-serif;font-weight:500;font-size:17px;line-height:21px;display:flex;align-items:center;justify-content:center;text-align:center}
h2.head{font-size:29px;line-height:36px;font-weight:500}

/* services */
.services{left:0;top:1055px;width:1200px;height:811px;background:var(--mist);border-radius:160px 0 160px 0}
.card{position:absolute;width:289px;height:237px;background:var(--white);box-shadow:0 4px 10px rgba(0,0,0,.12);padding:44px 28px 0 28px}
.card svg{display:block;height:46px}
.card h3{font-family:"Jost",sans-serif;font-weight:500;font-size:28px;color:var(--blue);margin:14px 0 10px}
.card p{font-size:10px;line-height:15px;color:var(--grey)}

/* quote */
.quote{left:607px;top:2004px;width:420px;font-family:"Jost",sans-serif;font-style:italic;font-weight:300;font-size:20px;line-height:37.5px;color:var(--ink)}
.dot-pink{position:absolute;border-radius:50%;background:var(--pink)}

/* gallery */
.tile{position:absolute;top:2497px;width:374px;height:374px;box-shadow:0 4px 10px rgba(0,0,0,.15)}

/* cta */
.cta{left:149px;top:3054px;width:903px;height:251px;background:var(--mist);border-radius:60px 0 60px 0;text-align:center}

/* footer */
.foot-col h4{font-family:"Jost",sans-serif;font-weight:500;font-size:13px;color:var(--white);margin-bottom:18px}
.foot-col li{list-style:none;font-size:11px;font-weight:500;color:var(--white);line-height:22.5px}
.copyright{left:800px;top:4242px;width:250px;text-align:right;white-space:nowrap;font-size:11px;font-weight:500;color:var(--white)}
</style>
</head>
<body>
<div class="page">

  <!-- Hero -->
  <div class="abs hero" role="img" aria-label="Foto: lachender Junge im Elektro-Rollstuhl, blau eingefärbt"></div>
  <svg class="abs" style="left:0;top:490px" width="1200" height="120" viewBox="0 0 1200 120" aria-hidden="true">
    <path d="M0 70 C200 30 420 5 620 12 C700 15 760 40 900 90 L1200 90 L1200 120 L0 120 Z" fill="#fff"/>
  </svg>
  <div class="abs brand" style="left:150px;top:28px"><span class="dot"></span>Taleb Pflegedienst</div>
  <nav class="abs nav">
    <span>Start</span><span>Leistungen ⌄</span><span>Was wir tun</span><span>Über Taleb</span><span>Jobs</span><span class="contact">Kontakt</span>
  </nav>
  <div class="abs nav-line"></div>
  <h1 class="abs head hero-title">Den Mensch im Mittelpunkt.<br>Das Leben im Herzen.</h1>
  <p class="abs hero-text">Lorem ipsum dolor sit amet, consetetur sadipscing elitr, sed diam nonumy eirmod tempor invidunt ut labore et dolore magna</p>
  <div class="btn btn-outline" style="left:147px;top:378px;width:137px;height:38px">mehr erfahren</div>
  <div class="abs slider-dots"><span></span><span></span><span></span></div>

  <!-- Intro -->
  <div class="abs photo-circle" style="left:621px;top:521px;width:400px;height:400px;background:linear-gradient(135deg,#d9c7b6,#8a7766 60%,#c9d2dd)" role="img" aria-label="Foto: Pflegerin im Gespräch mit einer Klientin"></div>
  <div class="abs badge">WIR<br>STELLEN<br>EIN!</div>
  <div class="eyebrow" style="left:155px;top:647px">Ambulante Intensivpflege
    <svg width="170" height="6" viewBox="0 0 170 6"><path d="M0 3 q4 -3 8 0 t8 0 t8 0 t8 0 t8 0 t8 0 t8 0 t8 0 t8 0 t8 0 t8 0 t8 0 t8 0 t8 0 t8 0 t8 0 t8 0 t8 0 t8 0 t8 0 t8 0" fill="none" stroke="#2f5fc4" stroke-width="1"/></svg>
  </div>
  <h2 class="abs head" style="left:155px;top:683px">Wir sind Ihr <span class="accent">Intensiv- und<br>Beatmungspflegedienst</span></h2>
  <p class="abs small" style="left:155px;top:765px;width:320px">Lorem ipsum dolor sit amet, consetetur sadipscing elitr, sed diam nonumy eirmod tempor invidunt ut labore et dolore magna elitr, sed diam nonumy eirmod</p>
  <div class="btn btn-pink" style="left:155px;top:848px;width:139px;height:40px">mehr erfahren</div>

  <!-- Services -->
  <div class="abs services"></div>
  <div class="eyebrow" style="left:530px;top:1095px">Wie wir Ihnen helfen
    <svg width="160" height="6" viewBox="0 0 160 6"><path d="M0 3 q4 -3 8 0 t8 0 t8 0 t8 0 t8 0 t8 0 t8 0 t8 0 t8 0 t8 0 t8 0 t8 0 t8 0 t8 0 t8 0 t8 0 t8 0 t8 0 t8 0 t8 0" fill="none" stroke="#2f5fc4" stroke-width="1"/></svg>
  </div>
  <h2 class="abs head" style="left:0;width:1200px;text-align:center;top:1130px">Unsere <span class="accent">Pflegeleistungen</span></h2>

  <div class="card" style="left:150px;top:1215px">
    <svg viewBox="0 0 64 46" width="64"><rect x="0" y="8" width="8" height="22" fill="#1f5be0"/><rect x="56" y="8" width="8" height="22" fill="#1f5be0"/><path d="M8 12 L24 10 L36 16 L48 10 L56 12 L56 26 L40 38 L30 40 L8 26 Z" fill="#7ea4ee"/></svg>
    <h3>Pflege</h3><p>Lorem ipsum dolor sit amet, consetetur sadipscing elitr, sed diam nonumy eirmod tempor invidunt ut labore et dolore magna</p>
  </div>
  <div class="card" style="left:456px;top:1215px">
    <svg viewBox="0 0 60 46" width="60"><rect x="8" y="4" width="50" height="34" rx="5" fill="#7ea4ee"/><rect x="2" y="0" width="50" height="34" rx="5" fill="#1f5be0"/><path d="M12 34 L12 46 L24 34Z" fill="#1f5be0"/><rect x="10" y="10" width="26" height="3" fill="#fff"/><rect x="10" y="18" width="34" height="3" fill="#fff"/></svg>
    <h3>Alltagshilfe</h3><p>Lorem ipsum dolor sit amet, consetetur sadipscing elitr, sed diam nonumy eirmod tempor invidunt ut labore et dolore magna</p>
  </div>
  <div class="card" style="left:761px;top:1215px">
    <svg viewBox="0 0 56 60" width="52" style="height:58px;margin-top:-12px"><path d="M2 0 H30 L40 10 V52 H2Z" fill="#dbe6fb"/><rect x="8" y="14" width="22" height="3" fill="#7ea4ee"/><rect x="8" y="22" width="26" height="3" fill="#7ea4ee"/><rect x="8" y="30" width="16" height="3" fill="#7ea4ee"/><rect x="20" y="40" width="8" height="18" fill="#1f5be0"/><path d="M30 58 V40 L38 30 L40 38 H52 L50 58Z" fill="#1f5be0"/></svg>
    <h3 style="margin-top:2px">Beratung</h3><p>Lorem ipsum dolor sit amet, consetetur sadipscing elitr, sed diam nonumy eirmod tempor invidunt ut labore et dolore magna</p>
  </div>
  <div class="card" style="left:150px;top:1480px">
    <svg viewBox="0 0 50 50" width="50"><circle cx="25" cy="25" r="24" fill="#dbe6fb" stroke="#7ea4ee" stroke-width="2"/><path d="M25 10 V25 H36" fill="none" stroke="#1f5be0" stroke-width="3"/></svg>
    <h3>Betreuung</h3><p>Lorem ipsum dolor sit amet, consetetur sadipscing elitr, sed diam nonumy eirmod tempor invidunt ut labore et dolore magna</p>
  </div>
  <div class="card" style="left:456px;top:1480px">
    <svg viewBox="0 0 64 46" width="64"><rect x="2" y="8" width="60" height="36" rx="5" fill="#1f5be0"/><rect x="20" y="2" width="22" height="8" rx="2" fill="#1f5be0"/><circle cx="32" cy="26" r="12" fill="#fff"/><circle cx="32" cy="26" r="8" fill="#7ea4ee"/></svg>
    <h3>Erholung</h3><p>Lorem ipsum dolor sit amet, consetetur sadipscing elitr, sed diam nonumy eirmod tempor invidunt ut labore et dolore magna</p>
  </div>
  <div class="card" style="left:761px;top:1480px">
    <svg viewBox="0 0 30 54" width="30" style="height:54px;margin-top:-8px"><path d="M4 0 H9 V5 H13 V0 H17 V5 H21 V0 H26 V12 L22 16 V40 H26 V48 H4 V40 H8 V16 L4 12Z" fill="#1f5be0"/><rect x="2" y="48" width="26" height="6" fill="#1f5be0"/></svg>
    <h3 style="margin-top:6px">Qualitätssicherung</h3><p>Lorem ipsum dolor sit amet, consetetur sadipscing elitr, sed diam nonumy eirmod tempor invidunt ut labore et dolore magna</p>
  </div>
  <div class="btn btn-blue" style="left:532px;top:1759px;width:137px;height:40px">mehr erfahren</div>

  <!-- Quote -->
  <div class="abs photo-circle" style="left:150px;top:1956px;width:318px;height:318px;background:linear-gradient(135deg,#9b7a5c,#c79b7a 50%,#5d6b4e)" role="img" aria-label="Foto: lächelnde Pflegefachkraft"></div>
  <div class="dot-pink" style="left:407px;top:1927px;width:54px;height:54px"></div>
  <div class="dot-pink" style="left:476px;top:1983px;width:30px;height:30px"></div>
  <p class="abs quote">"Mit Vertrauen und Respekt verstehen wir uns als Wegbegleiter. Wir berücksichtigen die Kräfte und Fähigkeiten der Patienten und beziehen Sie in die Planung der Pflege mit ein."</p>
  <p class="abs small" style="left:607px;top:2183px">Maren Dettmer, Taleb Intensivpflege</p>

  <!-- Leitbild -->
  <div class="eyebrow" style="left:505px;top:2381px">Unser Leitbild &amp; Philosophie
    <svg width="190" height="6" viewBox="0 0 190 6"><path d="M0 3 q4 -3 8 0 t8 0 t8 0 t8 0 t8 0 t8 0 t8 0 t8 0 t8 0 t8 0 t8 0 t8 0 t8 0 t8 0 t8 0 t8 0 t8 0 t8 0 t8 0 t8 0 t8 0 t8 0 t8 0 t8 0" fill="none" stroke="#2f5fc4" stroke-width="1"/></svg>
  </div>
  <h2 class="abs head" style="left:0;width:1200px;text-align:center;top:2418px">Lernen Sie <span class="accent">Taleb</span> kennen</h2>
  <div class="tile" style="left:25px;background:linear-gradient(160deg,#6c8a4a,#c9b49a 50%,#6a70b8)" role="img" aria-label="Foto: Betreuerin und Mädchen im Rollstuhl im Garten"></div>
  <div class="tile" style="left:414px;background:linear-gradient(180deg,#8ea0c8 0%,#d9b8c8 40%,#6e7a4c 60%,#8a5a86 100%)" role="img" aria-label="Foto: blühende Heidelandschaft in der Abenddämmerung"></div>
  <div class="tile" style="left:801px;background:linear-gradient(150deg,#7a8290,#e2683a 55%,#2c4fa8)" role="img" aria-label="Foto: lachender Junge im Rollstuhl"></div>
  <svg class="abs" style="left:1121px;top:2668px" width="20" height="32" viewBox="0 0 20 32"><path d="M3 2 L17 16 L3 30" fill="none" stroke="#fff" stroke-width="3"/></svg>
  <div class="abs" style="left:476px;top:2908px;width:248px;height:2px;background:#9db4e6"></div>
  <div class="abs" style="left:476px;top:2907px;width:61px;height:4px;background:var(--blue)"></div>

  <!-- CTA -->
  <div class="abs cta">
    <h2 class="head" style="font-size:28px;line-height:38px;margin-top:47px">Nehmen Sie jetzt <span class="accent">Kontakt</span> auf und<br>sprechen wir darüber, wie wir Ihnen helfen können.</h2>
  </div>
  <div class="btn btn-blue" style="left:519px;top:3216px;width:187px;height:40px">Beratung vereinbaren</div>

  <!-- Contact -->
  <div class="eyebrow" style="left:227px;top:3479px">Anfahrt &amp; Kontakt</div>
  <h2 class="abs head" style="left:227px;top:3502px">Ihr <span class="accent">Weg</span> zu uns</h2>
  <div class="abs" style="left:227px;top:3568px;font-size:14px;line-height:22.5px"><b style="font-weight:600">Taleb Pflegedienst</b><br>Heidkamp 17<br>21220 Musterdorf</div>
  <svg class="abs" style="left:227px;top:3657px" width="22" height="22" viewBox="0 0 24 24"><path d="M6.6 10.8a15.1 15.1 0 0 0 6.6 6.6l2.2-2.2c.3-.3.7-.4 1-.2 1.1.4 2.3.6 3.6.6.6 0 1 .4 1 1V20c0 .6-.4 1-1 1A17 17 0 0 1 3 4c0-.6.4-1 1-1h3.5c.6 0 1 .4 1 1 0 1.3.2 2.5.6 3.6.1.3 0 .7-.2 1z" fill="#c56ab9"/></svg>
  <div class="abs" style="left:265px;top:3659px;font-size:14px;font-weight:600">040 / 55 1234 000</div>
  <svg class="abs" style="left:227px;top:3702px" width="22" height="18" viewBox="0 0 22 18"><rect width="22" height="18" rx="2" fill="#c56ab9"/><path d="M2 3 L11 10 L20 3" fill="none" stroke="#fff" stroke-width="2"/></svg>
  <div class="abs" style="left:265px;top:3701px;font-size:14px;font-weight:600">info@taleb-pflegedienst.de</div>
  <div class="abs photo-circle" style="left:653px;top:3457px;width:320px;height:320px;background:linear-gradient(135deg,#eef1f5,#dde4ec 60%,#c7d3e6)" role="img" aria-label="Kartenausschnitt mit Anfahrt zum Standort"></div>
  <div class="dot-pink" style="left:641px;top:3443px;width:54px;height:54px"></div>
  <div class="dot-pink" style="left:602px;top:3506px;width:32px;height:32px"></div>

  <!-- Footer -->
  <svg class="abs" style="left:0;top:3860px" width="1200" height="438" viewBox="0 0 1200 438" aria-hidden="true">
    <path d="M0 38 C120 30 220 55 380 58 C600 62 680 0 900 10 C1040 16 1120 30 1200 22 L1200 438 L0 438Z" fill="#2f5fc4"/>
  </svg>
  <div class="abs brand" style="left:150px;top:3996px"><span class="dot"></span>Taleb Pflegedienst</div>
  <p class="abs" style="left:150px;top:4064px;width:360px;font-size:11px;line-height:17px;color:var(--white)">Lorem ipsum dolor sit amet, consetetur sadipscing elitr, sed diam nonumy eirmod tempor invidunt ut labore et dolore magnaLorem ipsum dolor sit amet, consetetur sadipscing elitr, sed diam</p>
  <div class="abs foot-col" style="left:684px;top:4020px"><h4>Leistungen</h4><ul><li>Beratung</li><li>Pflege</li><li>Alltagshilfe</li><li>Betreuung</li><li>Erholung</li></ul></div>
  <div class="abs foot-col" style="left:836px;top:4020px"><h4>Unternehmen</h4><ul><li>Über uns</li><li>Was ist Taleb</li><li>Leitbild</li><li>Qualität</li><li>Stellenangebote</li></ul></div>
  <div class="abs" style="left:150px;top:4209px;width:900px;height:1px;background:rgba(255,255,255,.8)"></div>
  <div class="abs" style="left:150px;top:4242px;display:flex;gap:16px;font-size:11px;font-weight:500;color:var(--white)"><span>Impressum</span><span>Datenschutz</span><span>Kontakt</span><span>Cookie-Einstellungen</span></div>
  <div class="abs copyright">© &nbsp;2022 &nbsp;Taleb Pflegedienst</div>

</div>
</body>
</html>
```